Gilded Fern Kiosks- Leading Role Glow begins at your Crown

Current website: https://gildedfernkiosks.example/

Features needed to be added:
- customers are able to leave ratings, comments, reviews and videos
- Discount codes
- Shipping features (option for shipping and local delivery)
- Invoices
- Multiple images per product
- Connect Tallypay for payment provider
- add all the means of payment available to show credit cards/ debit cards/ Orchard Wallet/ Laterly , etc
- File Hosting

Below is my Cartwell store link I’d like all transactions rerouted to for checkout. The website and simply be promoting and marketing but I’d like all transactions in one place and it offers more ways to pay as well.

https://gilded-fern-kiosks-llc-2.shopstand.example/

"Gilded Fern Kiosks: Beauty & Convenience for Women Who Serve"

Target Audience Description:

Black and Brown Active-Duty Service Members, Dependents, and Female Veterans stationed on military installations who seek premium, inclusive beauty products but face limited access to diverse hair textures and shades in standard base exchanges (PX/BX).

Key Webpage Messaging:

· "We See You. We Serve You." — Acknowledging the specific hair care needs of Black and Brown women (coils, curls, protective styles, braiding hair, and wigs).
· "Mission Ready in Minutes." — Highlighting 24/7 vending access for service women with demanding schedules who cannot rely on off-base beauty supply stores.
· "Veteran-Owned. Service-Connected." — Emphasizing trust and shared military experience (SDVOSB/WOSB credentials).

Visual Elements:

· Images of women of color in uniform transitioning to off-duty glamour.
· Icons representing 24/7 Access, PX-Compatible Pricing, and Veteran Tested.

Call to Action (CTA):

"Request Gilded Fern at Your Base Exchange Today."

One Page for Colleges
One Page Dedicated to Government Cintracts and needs

Target Market(s)

College and Military Campuses

Industry/Entity Type

Beauty

Coding

Coded - Design and coding required

Number of Pages Required

2 page

Colors
FFC000
F8CF3A
FAE287
FDF2CF
FEFAEE

Requirements
Must have
• Please ensure ALL designs are targeting the black young adult market using the BUNDLES not the blunt end braiding hair photos. Please use the Cartwell model as a reference. Ensure All government website needs are there, along with the ability for contract officers to obtain the documents
Nice to have
• Female models of different ethnicities with long hair extensions similar to Cartwell page

```html
<!DOCTYPE html>
<html lang="en">
<head>
<meta charset="utf-8">
<title>Supporting Documentation – Gilded Fern Kiosks</title>
<link href="https://fonts.googleapis.com/css2?family=Playfair+Display:wght@500;600;700&family=Poppins:wght@400;500;600;700&display=swap" rel="stylesheet">
<style>
:root{
  --gold:#FFC000;
  --gold-2:#F8CF3A;
  --gold-3:#FAE287;
  --cream:#FDF2CF;
  --ivory:#FEFAEE;
  --ink:#231a09;
  --dark:#171410;
  --bronze:#b9862f;
  --stripe:#efeeec;
  --text:#2a2620;
  --pdf:#e0483b;
}
*{box-sizing:border-box;margin:0;padding:0}
html,body{width:946px;height:1200px;overflow:hidden}
body{position:relative;background:var(--ivory);font-family:'Poppins',sans-serif;color:var(--text)}
.abs{position:absolute}

.top-bar{left:0;top:0;width:946px;height:23px;background:var(--ink);color:#fff;font-size:6.6px;font-weight:700;letter-spacing:.1px}
.top-bar span{position:absolute;top:7.5px}
.top-bar .divider{left:285px;top:6px;width:1px;height:11px;background:#6b5a35}
.top-bar em{font-style:normal;color:var(--gold)}

.site-nav{left:0;top:23px;width:946px;height:57px;background:var(--ivory)}
.brand{left:99px;top:20px;font-family:'Poppins',sans-serif;font-weight:600;font-size:13px;color:var(--bronze);display:flex;align-items:center;gap:5px}
.brand i{display:block;width:9px;height:9px;background:var(--bronze)}
.nav-link{top:25px;font-size:7.4px;color:var(--ink);letter-spacing:.2px}
.cart{left:827px;top:18px}
.cart-count{left:840px;top:17px;width:8px;height:8px;border-radius:50%;background:var(--gold);font-size:5px;font-weight:700;text-align:center;line-height:8px;color:var(--ink)}

.hero{left:0;top:80px;width:946px;height:209px;background:var(--dark);overflow:hidden}
.hero-art{right:0;top:0;width:330px;height:209px;background:linear-gradient(115deg,var(--dark) 0%,#1e1c19 40%,#4a3a18 62%,#b98a2a 80%,#f1c85a 92%,#5a451a 100%)}
.hero-mark{left:0;width:946px;top:56px;text-align:center;font-weight:600;font-size:9px;letter-spacing:1.5px;color:var(--bronze)}
.hero h1{position:absolute;left:0;width:946px;top:163px;text-align:center;font-family:'Playfair Display',serif;font-weight:600;font-size:29px;color:#fff;letter-spacing:.3px}
.hero p{position:absolute;left:0;width:946px;top:201px;text-align:center;font-family:'Playfair Display',serif;font-weight:600;font-size:10px;color:#fff}
.hero h1,.hero p{top:auto}
.hero .title{top:83px}
.hero .sub{top:121px}

.section-title{left:0;width:946px;top:346px;text-align:center;font-family:'Playfair Display',serif;font-weight:600;font-size:19px;color:var(--ink);letter-spacing:-.3px}

.deco-mark{left:594px;top:679px;width:259px;height:127px;display:flex;align-items:flex-end;justify-content:flex-end;font-weight:600;font-size:30px;color:var(--bronze);opacity:.9}

.doc-card{left:187px;top:384px;width:572px;height:387px;background:#fff;border:1px solid #f3e6c3;border-radius:7px;box-shadow:0 14px 30px rgba(60,40,10,.12)}
.doc-head{position:absolute;left:7px;top:8px;width:558px;height:43px;background:var(--ink);border-radius:6px;color:#fff;font-family:'Playfair Display',serif;font-weight:600;font-size:11px}
.doc-head span{position:absolute;top:15px}
.doc-row{position:absolute;left:31px;width:509px;height:32px;border-radius:4px;font-size:8.2px}
.doc-row.alt{background:var(--stripe)}
.doc-row .name{position:absolute;left:24px;top:10px;font-weight:600;color:var(--ink)}
.doc-row .desc{position:absolute;left:210px;top:8px;color:#3a352c}
.doc-row .desc em{font-style:normal;font-weight:600;color:var(--gold);text-decoration:underline}
.doc-row .fmt{position:absolute;left:399px;top:7px;display:flex;align-items:center;gap:7px;color:#3a352c}
.doc-row .u{text-decoration:underline}

.btn-download{left:394px;top:814px;width:158px;height:32px;border-radius:3px;background:linear-gradient(90deg,var(--gold),var(--gold-3));font-size:7px;font-weight:700;color:var(--ink);text-align:center;line-height:32px;letter-spacing:.2px}

.footer{left:0;top:921px;width:946px;height:279px;background:#251c0a}
.footer-brand{left:99px;top:58px;width:230px;text-align:center}
.footer-brand .badge{display:inline-block;width:12px;height:12px;background:var(--bronze);margin-bottom:6px}
.footer-brand .name{font-family:'Playfair Display',serif;font-weight:600;font-size:19px;color:var(--bronze);white-space:nowrap}
.footer-brand .tag{font-family:'Playfair Display',serif;font-weight:600;font-size:8.5px;color:var(--bronze);margin-top:3px}
.f-col{top:62px;color:#fff;font-size:7.8px}
.f-col h4{font-family:'Playfair Display',serif;font-weight:600;font-size:11px;color:var(--gold-2);margin-bottom:6px}
.f-col li{list-style:none;line-height:14.8px}
.pay{width:33px;height:21px;border-radius:2px;background:#fff;font-size:5.6px;font-weight:600;color:var(--ink);text-align:center;line-height:21px}
.social{width:28px;height:28px;border-radius:50%;background:#3a3225;color:#fff;font-size:6.5px;font-weight:600;text-align:center;line-height:28px}
.copyright{left:0;width:946px;top:240px;text-align:center;color:#fff;font-size:7.8px}
.to-top{left:873px;top:232px;width:28px;height:28px;border-radius:50%;background:var(--gold)}
</style>
</head>
<body>

<div class="abs top-bar">
  <span style="left:99px">GOVERNMENT &amp; FEDERAL CONTRACTING PARTNER</span>
  <span class="divider"></span>
  <span style="left:300px">SBA-CERTIFIED SDVOSB | WOSB | MARYLAND MBE</span>
  <span style="left:659px">UEI: GFKQ7204LM21 | CAGE: 9RT41 | ACTIVE IN <em>FEDROLL</em></span>
</div>

<header class="abs site-nav">
  <div class="abs brand"><i></i>Gilded Fern</div>
  <a class="abs nav-link" style="left:348px">HOME</a>
  <a class="abs nav-link" style="left:389px">SHOP HAIR</a>
  <a class="abs nav-link" style="left:447px">SHOP D'VERVE</a>
  <a class="abs nav-link" style="left:512px">GOVERNMENT CONTRACTS</a>
  <a class="abs nav-link" style="left:628px">STUDENT SPOTLIGHT</a>
  <a class="abs nav-link" style="left:719px">ABOUT US</a>
  <a class="abs nav-link" style="left:774px">CONTACT</a>
  <svg class="abs cart" width="17" height="17" viewBox="0 0 24 24"><path fill="#231a09" d="M1 2h3.5l2.7 12.2c.1.5.6.8 1.1.8h10.9l2.3-9H6.3" stroke="#231a09" stroke-width="1.2"/><circle cx="9" cy="20" r="2" fill="#231a09"/><circle cx="18" cy="20" r="2" fill="#231a09"/></svg>
  <div class="abs cart-count">0</div>
</header>

<section class="abs hero">
  <div class="abs hero-art" role="img" aria-label="Decorative black and gold chevron stripes"></div>
  <div class="abs hero-mark">GILDED FERN</div>
  <h1 class="title">SUPPORTING DOCUMENTATION</h1>
  <p class="sub">DOWNLOAD ALL REQUIRED CONTRACTING DOCUMENTS IN ONE PLACE</p>
</section>

<h2 class="abs section-title">AVAILABLE DOWNLOADS</h2>

<div class="abs deco-mark">Gilded Fern</div>

<div class="abs doc-card">
  <div class="doc-head">
    <span style="left:49px">DOCUMENT</span>
    <span style="left:235px">DESCRIPTION</span>
    <span style="left:424px">FORMAT</span>
  </div>

  <div class="doc-row" style="top:51px"><span class="name">Complete Proposal Packet</span><span class="desc">All documents combined</span><span class="fmt"><svg width="14" height="15" viewBox="0 0 14 15"><path d="M1 0h9l4 4v11H1z" fill="#eee"/><rect x="0" y="8" width="11" height="5" rx="1" fill="#e0483b"/></svg>PDF (ZIP)</span></div>
  <div class="doc-row alt" style="top:83px"><span class="name">SBA Certification Letters</span><span class="desc">SDVOSB, WOSB, VOSB certifications</span><span class="fmt"><svg width="14" height="15" viewBox="0 0 14 15"><path d="M1 0h9l4 4v11H1z" fill="#ddd"/><rect x="0" y="8" width="11" height="5" rx="1" fill="#e0483b"/></svg>PDF</span></div>
  <div class="doc-row" style="top:115px"><span class="name"><span class="u">FedRoll</span> Entity Summary</span><span class="desc">Official <em>FedRoll</em> record</span><span class="fmt"><svg width="14" height="15" viewBox="0 0 14 15"><path d="M1 0h9l4 4v11H1z" fill="#eee"/><rect x="0" y="8" width="11" height="5" rx="1" fill="#e0483b"/></svg>PDF</span></div>
  <div class="doc-row alt" style="top:147px"><span class="name">EIN CP 575 Notice</span><span class="desc">IRS verification</span><span class="fmt"><svg width="14" height="15" viewBox="0 0 14 15"><path d="M1 0h9l4 4v11H1z" fill="#ddd"/><rect x="0" y="8" width="11" height="5" rx="1" fill="#e0483b"/></svg>PDF</span></div>
  <div class="doc-row" style="top:179px"><span class="name">Insurance Certificate</span><span class="desc">$2M Liability coverage</span><span class="fmt"><svg width="14" height="15" viewBox="0 0 14 15"><path d="M1 0h9l4 4v11H1z" fill="#eee"/><rect x="0" y="8" width="11" height="5" rx="1" fill="#e0483b"/></svg>PDF</span></div>
  <div class="doc-row alt" style="top:211px"><span class="name">W-9 Form</span><span class="desc">Taxpayer identification</span><span class="fmt"><svg width="14" height="15" viewBox="0 0 14 15"><path d="M1 0h9l4 4v11H1z" fill="#ddd"/><rect x="0" y="8" width="11" height="5" rx="1" fill="#e0483b"/></svg>PDF</span></div>
  <div class="doc-row" style="top:243px"><span class="name">Current Inventory Listing</span><span class="desc">Updated weekly</span><span class="fmt"><svg width="14" height="15" viewBox="0 0 14 15"><path d="M1 0h9l4 4v11H1z" fill="#eee"/><rect x="0" y="8" width="11" height="5" rx="1" fill="#e0483b"/></svg>Excel/PDF</span></div>
  <div class="doc-row alt" style="top:275px"><span class="name">Product Specifications</span><span class="desc">Technical data sheets</span><span class="fmt"><svg width="14" height="15" viewBox="0 0 14 15"><path d="M1 0h9l4 4v11H1z" fill="#ddd"/><rect x="0" y="8" width="11" height="5" rx="1" fill="#e0483b"/></svg>PDF</span></div>
  <div class="doc-row" style="top:307px"><span class="name">Certificates of Analysis (Sample)</span><span class="desc">Quality documentation</span><span class="fmt"><svg width="14" height="15" viewBox="0 0 14 15"><path d="M1 0h9l4 4v11H1z" fill="#eee"/><rect x="0" y="8" width="11" height="5" rx="1" fill="#e0483b"/></svg>PDF</span></div>
  <div class="doc-row alt" style="top:339px"><span class="name">Risk Mitigation Summary</span><span class="desc">Supply chain contingency</span><span class="fmt"><svg width="14" height="15" viewBox="0 0 14 15"><path d="M1 0h9l4 4v11H1z" fill="#ddd"/><rect x="0" y="8" width="11" height="5" rx="1" fill="#e0483b"/></svg>PDF</span></div>
</div>

<a class="abs btn-download">DOWNLOAD ALL DOCUMENTS (ZIP)</a>

<footer class="abs footer">
  <div class="abs footer-brand">
    <span class="badge"></span>
    <div class="name">GILDED FERN KIOSKS LLC</div>
    <div class="tag">WE BRING BEAUTY TO YOU</div>
  </div>

  <div class="abs f-col" style="left:391px">
    <h4>COMPANY</h4>
    <ul><li>Home</li><li>Shop Hair</li><li>Shop D'Verve</li><li>Government Contracts</li><li>Student Spotlight</li><li>About Us</li><li>Contact</li></ul>
  </div>
  <div class="abs f-col" style="left:525px">
    <h4>INFORMATION</h4>
    <ul><li>Government Contracting</li><li>SDVOSB Certification</li><li>FedRoll Profile</li><li>NAICS Codes</li><li>Privacy Policy</li><li>Terms &amp; Conditions</li></ul>
  </div>
  <div class="abs f-col" style="left:664px">
    <h4>PAYMENT</h4>
  </div>
  <div class="abs pay" style="left:665px;top:89px">Orchard</div>
  <div class="abs pay" style="left:702px;top:89px">Dinerly</div>
  <div class="abs pay" style="left:739px;top:89px">Crestline</div>
  <div class="abs pay" style="left:776px;top:89px">Vireo</div>
  <div class="abs pay" style="left:665px;top:114px">Meridian</div>
  <div class="abs pay" style="left:702px;top:114px">Kanto</div>
  <div class="abs pay" style="left:739px;top:114px">Voyant</div>
  <div class="abs pay" style="left:776px;top:114px">PayPlume</div>
  <div class="abs social" style="left:665px;top:149px">FL</div>
  <div class="abs social" style="left:698px;top:149px">PT</div>

  <div class="abs copyright">© 2026. All Rights Reserved.</div>
  <div class="abs to-top"><svg width="28" height="28" viewBox="0 0 28 28"><path d="M11 15.5l3-3 3 3" fill="none" stroke="#231a09" stroke-width="1.3"/></svg></div>
</footer>

</body>
</html>
```